Scrapbooking company Vornello plain square mark

We need a cover design for our plain square mark page. We scrap and handmade projects. We would like to convey the idea of ​​creativity, creative workshop (cuts, paintings ...).

Font styles to use
Decorative
Script

```html
<!DOCTYPE html>
<html lang="en">
<head>
<meta charset="utf-8">
<title>Vornello – Page</title>
<link href="https://fonts.googleapis.com/css2?family=Roboto:wght@400;500;700&family=Arvo:wght@400;700&family=Bebas+Neue&display=swap" rel="stylesheet">
<style>
:root{
  --bar:#3b5998;
  --page:#e9ebee;
  --card:#ffffff;
  --line:#dddfe2;
  --text:#1d2129;
  --muted:#90949c;
  --link:#365899;
  --cta:#4a7cf7;
  --green:#42b72a;
  --soft:#f6f7f9;
  --wood-a:#b39a7e;
  --wood-b:#8c7358;
  --room-a:#e9e4dc;
  --room-b:#8d8f86;
  --orange:#f7941d;
  --teal:#2fb5b0;
  --cream:#fff8ea;
}
*{box-sizing:border-box;margin:0;padding:0}
html,body{width:1200px;height:844px;overflow:hidden}
body{background:var(--page);font-family:"Roboto",Helvetica,Arial,sans-serif;color:var(--text);position:relative;font-size:12px}
.abs{position:absolute}
.card{position:absolute;background:var(--card);border:1px solid var(--line);border-radius:3px}

/* top bar */
.topbar{position:absolute;left:0;top:0;width:1200px;height:38px;background:var(--bar)}
.topbar .mark{left:131px;top:8px;width:22px;height:22px;background:#fff;border-radius:2px}
.topbar .search{left:162px;top:7px;width:395px;height:21px;background:#fff;border-radius:2px;font-size:13px;padding:3px 10px;color:var(--text)}
.topbar .search-btn{right:0;top:0;width:42px;height:21px;background:var(--soft);border-left:1px solid var(--line)}
.topbar .me{left:733px;top:7px;width:18px;height:18px;background:linear-gradient(#8a7260,#3e322b);border-radius:2px}
.topbar .name{top:11px;color:#fff;font-size:12px;font-weight:700}
.topbar .icon{top:10px;width:18px;height:16px;background:#fff;opacity:.9;border-radius:8px}

/* left column */
.profile-pic{left:133px;top:49px;width:150px;height:149px;background:#fff;border:1px solid var(--line);padding:3px}
.profile-pic .fill{width:100%;height:100%;background:repeating-linear-gradient(90deg,var(--wood-a) 0 26px,var(--wood-b) 26px 28px);display:flex;align-items:center;justify-content:center}
.profile-pic .brand{font-family:"Bebas Neue",sans-serif;color:var(--teal);font-size:30px;background:var(--cream);padding:2px 10px}
.page-name{left:132px;top:208px;font-size:22px;line-height:24px;color:var(--text)}
.verified{display:inline-block;width:17px;height:17px;border-radius:50%;background:#4080ff;vertical-align:-2px;margin-left:2px;position:relative}
.page-handle{left:133px;top:259px;font-size:13px;color:var(--muted)}
.side-nav{left:131px;top:292px;width:156px;list-style:none}
.side-nav li{height:28.4px;line-height:28.4px;padding-left:9px;font-size:13.5px;color:#4b4f56}
.side-nav li.active{background:#dcdee3;border-left:3px solid var(--bar);padding-left:7px;color:var(--text);font-weight:500;height:29px}
.create-btn{left:139px;top:506px;width:88px;height:21px;background:var(--green);color:#fff;font-weight:700;font-size:11.5px;text-align:center;line-height:21px;border-radius:2px}

/* cover */
.cover{position:absolute;overflow:hidden}
.cover .room{position:absolute;inset:0;background:linear-gradient(100deg,var(--room-a) 40%,#c9c6bd 60%,var(--room-b) 100%)}
.cover .wood{position:absolute;inset:0;background:repeating-linear-gradient(93deg,var(--wood-a) 0 70px,var(--wood-b) 70px 73px,#a88e72 73px 140px)}
.cover .title{position:absolute;border:3px solid #fff;color:#fff;text-align:left}
.cover .t1{font-family:"Arvo",serif;display:block;letter-spacing:1px}
.cover .t3{font-family:"Bebas Neue",sans-serif;display:block}
.cover .logo-name{position:absolute;font-family:"Bebas Neue",sans-serif;color:var(--teal);background:var(--cream);text-align:center;border-radius:8px}
.cover .band{position:absolute;background:var(--orange);color:#fff;font-family:"Roboto",sans-serif;display:flex;align-items:center}
.cover .band span{display:inline-flex;align-items:center}

/* action bar */
.actions{left:295px;top:316px;width:736px;height:47px;border-top:none;border-radius:0 0 3px 3px}
.btn-grp{position:absolute;left:11px;top:12px;display:flex;border:1px solid #ccd0d5;border-radius:2px;background:var(--soft)}
.btn-grp div{height:24px;line-height:23px;font-size:12px;font-weight:700;color:#4b4f56;padding:0 9px;border-right:1px solid #ccd0d5;display:flex;align-items:center;gap:5px}
.btn-grp div:last-child{border-right:none}
.caret{width:0;height:0;border:4px solid transparent;border-top-color:#4b4f56;margin-top:4px}
.contact{position:absolute;left:459px;top:12px;width:265px;height:25px;background:var(--cta);color:#fff;font-size:13px;text-align:center;line-height:25px;border-radius:2px}

/* composer */
.composer{left:295px;top:376px;width:446px;height:95px}
.composer .head{height:29px;background:var(--soft);border-bottom:1px solid var(--line);display:flex;align-items:center;padding-left:16px;gap:6px;font-size:12px}
.composer .head .link{color:var(--link)}
.avatar{position:absolute;background:linear-gradient(160deg,#c8b9a8,#5b4a3f);border-radius:2px}
.placeholder{position:absolute;color:var(--muted);font-size:13.5px}

/* post */
.post{left:295px;top:481px;width:446px;height:380px}
.post .who{position:absolute;left:53px;top:20px;font-size:13px;color:var(--text)}
.post .who b{color:var(--link);font-weight:400;font-size:14px}
.post .who a{color:var(--link);text-decoration:none;font-size:12px}
.post .time{position:absolute;left:53px;top:38px;font-size:11.5px;color:var(--muted)}
.post-actions{position:absolute;left:10px;top:236px;width:426px;height:32px;border-top:1px solid var(--line);display:flex;gap:30px;padding-left:5px;align-items:center;font-size:12px;color:#4b4f56}
.post-actions span{display:flex;align-items:center;gap:6px}
.reacts{position:absolute;left:0;top:269px;width:444px;height:41px;background:var(--soft);border-top:1px solid var(--line)}
.reacts .dot{position:absolute;top:13px;width:15px;height:15px;border-radius:50%;border:1.5px solid #fff}
.reacts .count{position:absolute;left:60px;top:13px;color:var(--link);font-size:12px}
.reacts .top{position:absolute;right:14px;top:13px;color:var(--link);font-size:12px}
.comment-box{position:absolute;left:48px;top:313px;width:387px;height:32px;border:1px solid #ccd0d5;border-radius:2px;color:var(--muted);font-size:13px;padding:8px 12px}

/* right column */
.side-card{left:754px;width:277px}
.side-card .label{font-size:13.5px;color:var(--text)}
.sec-head{height:31px;border-bottom:1px solid var(--line);font-size:11px;font-weight:500;color:#4b4f56;padding:10px 8px;position:relative}
.chev{position:absolute;right:10px;top:10px;width:8px;height:8px;border-right:2px solid #606770;border-top:2px solid #606770;transform:rotate(45deg)}
.about-text{position:absolute;left:30px;top:50px;font-size:12px;line-height:15.5px;color:var(--text);width:240px}
.about-link{position:absolute;left:30px;top:107px;font-size:11.5px;color:var(--link)}
.mini-dot{position:absolute;width:9px;height:9px;border-radius:50%;border:1px solid #bec3c9}
.photo-grid{position:absolute;left:6px;top:30px;display:grid;grid-template-columns:85px 85px 86px;gap:5px 6px}
.photo-grid div{height:79px;background:#5790f9}
</style>
</head>
<body>

<header class="topbar">
  <div class="abs mark"></div>
  <div class="abs search">Vornello
    <div class="abs search-btn">
      <svg width="42" height="21" viewBox="0 0 42 21"><circle cx="20" cy="9.5" r="4.5" fill="none" stroke="#606770" stroke-width="1.5"/><line x1="23.5" y1="13" x2="26.5" y2="16" stroke="#606770" stroke-width="1.5"/></svg>
    </div>
  </div>
  <div class="abs me" role="img" aria-label="Profile photo of the signed-in user"></div>
  <div class="abs name" style="left:758px">Alex Marlow</div>
  <div class="abs name" style="left:832px">Home</div>
  <svg class="abs" style="left:889px;top:9px" width="110" height="20" viewBox="0 0 110 20" fill="#fff">
    <circle cx="6" cy="6" r="3.5"/><path d="M0 17c0-5 12-5 12 0z"/><circle cx="13" cy="5" r="3"/><path d="M10 14c1-4 10-4 10 1z"/>
    <rect x="32" y="4" width="14" height="10" rx="1.5"/><path d="M36 14l-2 4 5-4z"/><rect x="40" y="1" width="10" height="7" rx="1.5" opacity=".8"/>
    <circle cx="69" cy="9" r="8"/><path d="M65 5c2 2 1 4 3 5s-1 4 1 5M72 3c-1 2 2 3 3 5" stroke="#3b5998" stroke-width="1.5" fill="none"/>
    <rect x="88" y="2" width="1" height="16" opacity=".4"/>
  </svg>
  <svg class="abs" style="left:1000px;top:12px" width="36" height="14" viewBox="0 0 36 14" fill="#fff">
    <rect x="0" y="3" width="14" height="9" rx="1"/><rect x="3" y="0" width="8" height="4" rx="1" fill="none" stroke="#fff" stroke-width="1.5"/>
    <path d="M22 4h10l-5 6z"/>
  </svg>
</header>

<!-- left column -->
<div class="abs profile-pic">
  <div class="fill" role="img" aria-label="Profile picture: brand name on a light wooden board background">
    <span class="brand">Vornello</span>
  </div>
</div>
<h1 class="abs page-name" style="font-weight:400">Vornello<br>Crafts <span class="verified"><svg width="17" height="17" viewBox="0 0 17 17"><path d="M5 8.5l2.5 2.5 4.5-5" stroke="#fff" stroke-width="2" fill="none"/></svg></span></h1>
<div class="abs page-handle">@vornello</div>
<ul class="abs side-nav">
  <li class="active">Home</li>
  <li>Photos</li>
  <li>Likes</li>
  <li>About</li>
  <li>Videos</li>
  <li>Welcome</li>
  <li>Posts</li>
</ul>
<div class="abs create-btn">Create a Page</div>

<!-- cover -->
<section class="cover" style="left:295px;top:38px;width:736px;height:278px">
  <div class="room" role="img" aria-label="Photo of a bright craft studio with shelves of coloured supplies"></div>
  <div class="wood" role="img" aria-label="Weathered wooden plank texture" style="clip-path:polygon(0 0,358px 0,335px 278px,0 278px)"></div>
  <div class="title" style="left:35px;top:64px;width:237px;height:156px;padding:6px 10px">
    <span class="t1" style="font-size:44px;line-height:40px">SCRAP &amp;</span>
    <span class="t1" style="font-size:31px;line-height:30px">HANDMADE</span>
    <span class="t3" style="font-size:80px;line-height:72px">PROJECTS</span>
  </div>
  <div class="logo-name" style="left:432px;top:130px;width:230px;font-size:52px;line-height:62px">Vornello</div>
  <div class="band" style="left:309px;top:217px;width:427px;height:38px;clip-path:polygon(10px 0,100% 0,100% 100%,0 100%);font-size:16px">
    <span style="position:absolute;left:86px"><svg width="18" height="18" viewBox="0 0 18 18" style="margin-right:4px"><path d="M4 2l3 3-2 2c1 2 3 4 5 5l2-2 3 3-2 3C7 15 3 11 1 4z" fill="none" stroke="#fff" stroke-width="1.5"/></svg>55501234</span>
    <span style="position:absolute;left:248px"><svg width="17" height="17" viewBox="0 0 17 17" style="margin-right:5px"><circle cx="8.5" cy="8.5" r="7" fill="none" stroke="#fff" stroke-width="1.4"/><ellipse cx="8.5" cy="8.5" rx="3" ry="7" fill="none" stroke="#fff" stroke-width="1.2"/><line x1="1.5" y1="8.5" x2="15.5" y2="8.5" stroke="#fff" stroke-width="1.2"/></svg>vornello.com</span>
  </div>
</section>

<div class="card actions">
  <div class="btn-grp">
    <div><svg width="13" height="12" viewBox="0 0 13 12"><rect x="0" y="5" width="3" height="7" fill="#4267b2"/><path d="M4 5l3-5c2 0 2 2 1 4h4v4l-2 4H4z" fill="#4267b2"/></svg>Liked<span class="caret"></span></div>
    <div><svg width="13" height="13" viewBox="0 0 13 13"><circle cx="6.5" cy="6" r="6" fill="#90949c"/></svg>Message</div>
    <div><span style="color:#90949c;letter-spacing:1px">···</span>More<span class="caret"></span></div>
  </div>
  <div class="contact">Contact Us</div>
</div>

<!-- composer -->
<div class="card composer">
  <div class="head">
    <svg width="16" height="14" viewBox="0 0 16 14"><path d="M2 12l2-4 7-7 2 2-7 7z" fill="#4267b2"/></svg>
    <span style="margin-left:6px">Status</span>
    <svg width="16" height="14" viewBox="0 0 16 14" style="margin-left:4px"><rect x="1" y="2" width="14" height="11" rx="1" fill="#90949c"/><circle cx="8" cy="7.5" r="3" fill="#fff"/></svg>
    <span class="link">Photo / Video</span>
    <span class="avatar" style="left:412px;top:6px;width:14px;height:14px" role="img" aria-label="Posting-as profile photo"></span>
    <span class="caret abs" style="left:432px;top:8px"></span>
  </div>
  <div class="avatar" style="left:11px;top:39px;width:37px;height:37px" role="img" aria-label="Profile photo of the signed-in user"></div>
  <div class="placeholder" style="left:57px;top:105px;top:105px;top:104px;top:104px;top:104px;top:104px;top:104px;top:104px;top:104px;top:104px;top:104px;top:104px;top:104px;top:104px;top:104px;top:104px;top:104px;top:104px;top:104px;top:104px;top:104px;top:104px;top:104px;top:104px;top:104px;top:104px;top:104px;top:104px;top:104px;top:104px;top:49px">Write something on this Page...</div>
</div>

<!-- post -->
<article class="card post">
  <div class="abs" style="left:10px;top:13px;width:36px;height:36px;background:repeating-linear-gradient(90deg,var(--wood-a) 0 8px,var(--wood-b) 8px 9px)" role="img" aria-label="Page profile picture thumbnail"></div>
  <div class="who"><b>Vornello Crafts</b> changed their <a>cover photo</a>.</div>
  <div class="time">2 mins · <svg width="10" height="10" viewBox="0 0 10 10" style="vertical-align:-1px"><circle cx="5" cy="5" r="4.5" fill="#90949c"/></svg></div>
  <div class="abs" style="right:12px;top:28px;width:7px;height:7px;border-right:1.5px solid #bec3c9;border-bottom:1.5px solid #bec3c9;transform:rotate(45deg)"></div>

  <div class="cover" style="left:10px;top:61px;width:428px;height:164px">
    <div class="room" role="img" aria-label="Photo of a bright craft studio with shelves of coloured supplies"></div>
    <div class="wood" role="img" aria-label="Weathered wooden plank texture" style="clip-path:polygon(0 0,208px 0,195px 164px,0 164px)"></div>
    <div class="title" style="left:20px;top:38px;width:138px;height:93px;padding:3px 5px;border-width:2px">
      <span class="t1" style="font-size:26px;line-height:24px">SCRAP &amp;</span>
      <span class="t1" style="font-size:18px;line-height:17px">HANDMADE</span>
      <span class="t3" style="font-size:47px;line-height:43px">PROJECTS</span>
    </div>
    <div class="logo-name" style="left:251px;top:77px;width:134px;font-size:31px;line-height:36px;border-radius:5px">Vornello</div>
    <div class="band" style="left:180px;top:128px;width:248px;height:22px;clip-path:polygon(6px 0,100% 0,100% 100%,0 100%);font-size:9.5px">
      <span style="position:absolute;left:50px"><svg width="10" height="10" viewBox="0 0 18 18" style="margin-right:3px"><path d="M4 2l3 3-2 2c1 2 3 4 5 5l2-2 3 3-2 3C7 15 3 11 1 4z" fill="none" stroke="#fff" stroke-width="2"/></svg>55501234</span>
      <span style="position:absolute;left:144px"><svg width="10" height="10" viewBox="0 0 17 17" style="margin-right:3px"><circle cx="8.5" cy="8.5" r="7" fill="none" stroke="#fff" stroke-width="2"/></svg>vornello.com</span>
    </div>
  </div>

  <div class="post-actions">
    <span><svg width="13" height="12" viewBox="0 0 13 12"><rect x="0" y="5" width="3" height="7" fill="#90949c"/><path d="M4 5l3-5c2 0 2 2 1 4h4v4l-2 4H4z" fill="#90949c"/></svg>Like</span>
    <span><svg width="13" height="12" viewBox="0 0 13 12"><path d="M0 0h13v9H5l-3 3V9H0z" fill="#90949c"/></svg>Comment</span>
    <span><svg width="15" height="12" viewBox="0 0 15 12"><path d="M9 0l6 5-6 5V7C5 7 2 8 0 12 1 6 4 3 9 3z" fill="#90949c"/></svg>Share</span>
    <span class="avatar" style="left:436px;top:9px;width:16px;height:16px;left:auto;right:6px" role="img" aria-label="Sharing-as profile photo"></span>
  </div>

  <div class="reacts">
    <span class="dot" style="left:10px;background:#4080ff"></span>
    <span class="dot" style="left:22px;background:#f0284a"></span>
    <span class="dot" style="left:34px;background:#fcd440"></span>
    <span class="count">1.6M</span>
    <span class="top">Top Comments <span class="caret" style="display:inline-block;border-width:3px;vertical-align:0"></span></span>
  </div>
  <div class="avatar" style="left:11px;top:313px;width:31px;height:31px" role="img" aria-label="Profile photo of the signed-in user"></div>
  <div class="comment-box">Write a comment...
    <svg class="abs" style="right:12px;top:8px" width="40" height="15" viewBox="0 0 40 15"><rect x="0" y="3" width="14" height="10" rx="1.5" fill="#bec3c9"/><circle cx="7" cy="8" r="2.5" fill="#fff"/><circle cx="32" cy="7.5" r="6" fill="none" stroke="#bec3c9" stroke-width="1.4"/><path d="M29.5 9c1.5 1.5 3.5 1.5 5 0" stroke="#bec3c9" fill="none"/></svg>
  </div>
</article>

<!-- right column -->
<div class="card side-card" style="top:376px;height:38px;padding:11px 10px"><span class="label">Personal Website</span></div>
<div class="card side-card" style="top:424px;height:35px;padding:9px 10px">
  <svg width="14" height="14" viewBox="0 0 14 14" style="vertical-align:-2px"><circle cx="5.5" cy="5.5" r="4.5" fill="none" stroke="#90949c" stroke-width="1.5"/><line x1="9" y1="9" x2="13" y2="13" stroke="#90949c" stroke-width="1.5"/></svg>
  <span style="color:var(--muted);font-size:13.5px;margin-left:8px">Search for Posts on the Page</span>
</div>
<div class="card side-card" style="top:469px;height:89px">
  <div class="avatar" style="left:12px;top:5px;width:30px;height:35px" role="img" aria-label="Friend profile photo"></div>
  <div class="abs" style="left:46px;top:7px;font-size:12.5px">1,955,550 people like this</div>
  <div class="abs" style="left:46px;top:25px;font-size:12.5px;color:var(--muted)">Sam Reed and 20 other friends</div>
  <div class="abs" style="left:0;top:45px;width:275px;border-top:1px solid var(--line)"></div>
  <svg class="abs" style="left:13px;top:59px" width="18" height="15" viewBox="0 0 18 15" fill="#bec3c9"><circle cx="6" cy="4" r="3.5"/><path d="M0 14c0-6 12-6 12 0z"/><path d="M14 3v6M11 6h6" stroke="#bec3c9" stroke-width="1.5"/></svg>
  <div class="abs" style="left:48px;top:60px;font-size:11.5px">Invite friends to like this Page</div>
</div>
<div class="card side-card" style="top:569px;height:123px">
  <div class="sec-head">ABOUT<span class="chev"></span></div>
  <span class="mini-dot" style="left:12px;top:55px"></span>
  <div class="about-text">Lorem ipsum dolor sit amet timeti ergo sum Lorem ipsum dolor sit amet timeti dolor sit amet timeti imeti ergo sum imeti ergo sum</div>
  <span class="mini-dot" style="left:12px;top:112px"></span>
  <div class="about-link">http://www.paperfold-studio.com/</div>
</div>
<div class="card side-card" style="top:707px;height:150px">
  <div class="sec-head">PHOTOS<span class="chev"></span></div>
  <div class="photo-grid">
    <div></div><div></div><div></div>
    <div></div><div></div><div></div>
  </div>
</div>

</body>
</html>
```